Electrical company business card design.

Hi, were an electrical company in Auckland New Zealand called Quarneth Ltd. We focus mainly on high end residential and commercial so the card would be targeted towards that.
The card will be for myself, i am the director of the company.
Name: Derek Olstow
Position: Director/electrician
Phone: 021 387 9415
Email: derek@quarneth.co.nz
Location: Auckland
As for colors the the blue color in the logo is preferred, i also don't mind a black background option.
Target Market(s)
High end residential and commercial
Industry/Entity Type
Electrician
Contact Information for Business Card
Name: Derek Olstow Position: Director/Electrician Phone: 021 387 9415, Email: derek@quarneth.co.nz, Location: Auckland

```html
<!DOCTYPE html>
<html lang="en">
<head>
<meta charset="utf-8">
<title>Quarneth Ltd – Business Card</title>
<link rel="stylesheet" href="https://fonts.googleapis.com/css2?family=Tinos:wght@400;700&display=swap">
<style>
  :root {
    --backdrop: #d1d2d4;
    --card: #ffffff;
    --navy: #1f4a99;
    --bright-blue: #035ba8;
    --ink: #1a1a1a;
    --icon: #1f4a99;
    --logo-grey: #4a4f5a;
    --ghost: rgba(90, 96, 112, 0.55);
    --ghost-faint: rgba(90, 96, 112, 0.18);
  }
  * { margin: 0; padding: 0; box-sizing: border-box; }
  html, body {
    width: 1200px; height: 1200px; overflow: hidden;
    background: var(--backdrop);
    font-family: "Tinos", "Times New Roman", serif;
  }
  .card {
    position: absolute; left: 265px;
    width: 1079px; height: 616px;
    background: var(--card);
    border-radius: 12px; overflow: hidden;
    transform: scale(0.6211); transform-origin: top left;
  }
  .card--front { top: 201px; }
  .card--back { top: 616px; }
  .card__bands { position: absolute; inset: 0; width: 100%; height: 100%; }
  .band--navy { fill: var(--navy); }
  .band--bright { fill: var(--bright-blue); }

  .brand-name {
    position: absolute; font-family: "Tinos", "Times New Roman", serif;
    font-weight: 700; white-space: nowrap; line-height: 1;
  }
  .brand-name--ghost { color: var(--ghost-faint); font-size: 56px; left: 40px; }
  .brand-name--mid { color: var(--ghost); font-size: 60px; left: 40px; top: 280px; }
  .brand-name--top { top: 52px; }
  .brand-name--bottom { top: 512px; }
  .brand-name--primary { color: var(--logo-grey); font-size: 84px; left: 60px; top: 262px; }
  .brand-name--panel { color: var(--ghost); font-size: 96px; left: 600px; top: 256px; }

  .contact { position: absolute; right: 69px; color: var(--ink); text-align: right; white-space: nowrap; line-height: 1; }
  .contact__name { top: 32px; font-size: 52px; font-weight: 700; }
  .contact__role { top: 92px; font-size: 50px; }
  .contact__phone { top: 248px; right: 136px; font-size: 50px; }
  .contact__email { top: 312px; right: 136px; font-size: 50px; }
  .contact__city { top: 500px; font-size: 50px; }

  .icon { position: absolute; fill: none; stroke: var(--icon); }
  .icon--phone { left: 958px; top: 245px; width: 54px; height: 54px; }
  .icon--mail { left: 963px; top: 322px; width: 46px; height: 34px; }
  .icon--pin { left: 893px; top: 428px; width: 36px; height: 52px; }
</style>
</head>
<body>

<section class="card card--front" aria-label="Business card front">
  <svg class="card__bands" viewBox="0 0 1079 616" preserveAspectRatio="none" aria-hidden="true">
    <polygon class="band--navy" points="0,0 471,0 313,616 0,616"/>
    <polygon class="band--navy" points="480,0 518,0 361,616 323,616"/>
    <polygon class="band--bright" points="528,0 566,0 408,616 370,616"/>
  </svg>
  <div class="brand-name brand-name--ghost brand-name--top" aria-hidden="true">Quarneth</div>
  <div class="brand-name brand-name--mid">Quarneth</div>
  <div class="brand-name brand-name--ghost brand-name--bottom" aria-hidden="true">Quarneth</div>

  <div class="contact contact__name">Derek Olstow</div>
  <div class="contact contact__role">Director</div>
  <div class="contact contact__phone">021 387 9415</div>
  <svg class="icon icon--phone" viewBox="0 0 54 54" aria-hidden="true">
    <path d="M8 6 L17 4 L22 15 L16 20 Q22 32 33 38 L38 32 L49 37 L47 46 Q40 52 30 46 Q12 36 6 18 Q4 10 8 6 Z" fill="var(--icon)" stroke="none"/>
    <path d="M30 8 Q42 10 45 22" stroke-width="4" stroke-linecap="round"/>
    <path d="M32 1 Q50 4 52 22" stroke-width="4" stroke-linecap="round"/>
  </svg>
  <div class="contact contact__email">derek@quarneth.co.nz</div>
  <svg class="icon icon--mail" viewBox="0 0 46 34" aria-hidden="true">
    <rect x="2" y="2" width="42" height="30" stroke-width="3.5"/>
    <path d="M2 2 L23 20 L44 2 M2 32 L18 16 M44 32 L28 16" stroke-width="3"/>
  </svg>
  <svg class="icon icon--pin" viewBox="0 0 36 52" aria-hidden="true">
    <path d="M18 2 C8 2 2 9 2 18 C2 30 18 50 18 50 C18 50 34 30 34 18 C34 9 28 2 18 2 Z M18 11 A7 7 0 1 0 18.01 11 Z" fill="var(--icon)" fill-rule="evenodd" stroke="none"/>
  </svg>
  <div class="contact contact__city">Auckland</div>
</section>

<section class="card card--back" aria-label="Business card back">
  <svg class="card__bands" viewBox="0 0 1079 616" preserveAspectRatio="none" aria-hidden="true">
    <polygon class="band--bright" points="413,0 451,0 610,616 573,616"/>
    <polygon class="band--navy" points="461,0 498,0 656,616 619,616"/>
    <polygon class="band--navy" points="508,0 1079,0 1079,616 666,616"/>
  </svg>
  <div class="brand-name brand-name--primary">Quarneth</div>
  <div class="brand-name brand-name--panel" aria-hidden="true">Quarneth</div>
</section>

</body>
</html>
```